Design Our Full Stationary Set

Hi, I require a selection of complimentary stationary as outlined below. The winning design to be provided .eps and .svg of each. We are in the advertising sphere, the winning design should be artistic, colourful, attractive and grab your attention. Files attached.

All should be 300 DPI

Business Card - 2 Sides
Full Bleed Size 88x58mm (1040x685 pixels)
Safe Margin Size for Text 85x55mm (1004x650 pixels)

Folder
Full Bleed Size 53x42.4cm (6260x5004 pixels)
Safe Margin Size for Text 52.7x42.1cm (6225x4969 pixels)

Address Label
Full Bleed Size 90x52mm (1062x615 pixels)
Safe Margin Size for Text 87x49mm (1028x579 pixels)

Envelope Seal (CIRCLE)
Full Bleed Size 43mm diameter (510 pixels)
Safe Margin Size for Text 38mm diameter (450 pixels)

Letterhead
Full Bleed Size 213x300mm (2517x3544 pixels)
Safe Margin Size for Text 210x297mm (2480x3580 pixels)

INFORMATION:

Company Name: Velkin Hartwell Ltd.
Company Website: www.velkin-hartwell.example
Company No.: 7KQT58
Address:
27 Brenlow Court, Tullagesh, Kildare, Ireland, R9QT604.
Name: Colm Brestwick
Title: Chief Executive Officer
Email: cbrestwick@velkin-hartwell.example
Phone: 00353-87-6207394

Target Market(s)

Advertisers and Marketers

Font styles to use
Serif
Script

Requirements
Must have
• Must fit dimensions given
Nice to have
• Colours that compliment our logo.

```html
<!DOCTYPE html>
<html lang="en">
<head>
<meta charset="utf-8">
<title>Velkin Hartwell – Business Card</title>
<link href="https://fonts.googleapis.com/css2?family=Source+Sans+3:wght@400;600&display=swap" rel="stylesheet">
<style>
  :root {
    --backdrop: #3b3431;
    --card: #141414;
    --card-back: #0c0c0c;
    --ink: #ffffff;
    --ink-soft: #dcdcdc;
    --accent: #e0158c;
    --silver: #bdbdbd;
    --rule: #6a6a6a;
  }
  * { margin: 0; padding: 0; box-sizing: border-box; }
  html, body {
    width: 1200px; height: 814px; overflow: hidden;
    background: var(--backdrop);
    font-family: "Source Sans 3", "Helvetica Neue", Arial, sans-serif;
  }
  .stage { position: relative; width: 1200px; height: 814px; }
  .card {
    position: absolute; top: 227px;
    width: 545px; height: 360px;
    border-radius: 4px;
    box-shadow: 0 10px 28px rgba(0,0,0,.45);
  }
  .card--front { left: 40px; background: var(--card); color: var(--ink); }
  .card--back { left: 615px; background: var(--card-back); }

  .wordmark {
    display: flex; align-items: center; gap: 14px;
    font-weight: 400; letter-spacing: 6px; text-transform: uppercase;
    white-space: nowrap;
  }
  .wordmark__dot { width: 18px; height: 18px; border-radius: 50%; flex: none; }

  .card--front .wordmark {
    position: absolute; top: 92px; left: 0; right: 0; justify-content: center;
    font-size: 32px; color: var(--ink);
  }
  .card--front .wordmark__dot { background: var(--accent); }

  .person {
    position: absolute; left: 16px; top: 205px; width: 270px;
    text-align: right; line-height: 1.32;
  }
  .person__name { font-size: 20px; font-weight: 600; }
  .person__title { font-size: 16px; color: var(--accent); }
  .person__line { font-size: 15.5px; color: var(--ink-soft); }

  .divider {
    position: absolute; left: 298px; top: 178px; width: 1px; height: 126px;
    background: var(--rule);
  }
  .company {
    position: absolute; left: 312px; top: 178px; width: 218px;
    font-size: 14px; line-height: 1.45; color: var(--ink-soft);
  }
  .company__row { display: flex; align-items: center; gap: 7px; white-space: nowrap; }
  .company__row svg { flex: none; }

  .card--back .wordmark {
    position: absolute; top: 150px; left: 0; right: 0; justify-content: center;
    font-size: 32px; color: var(--silver);
  }
  .card--back .wordmark__dot { background: var(--silver); }
  .card--back .site {
    position: absolute; top: 228px; left: 0; right: 0; text-align: center;
    font-size: 12px; letter-spacing: 2px; color: var(--silver);
  }
</style>
</head>
<body>
<main class="stage">
  <section class="card card--front">
    <div class="wordmark"><span>Velkin Hartwell</span><span class="wordmark__dot"></span></div>

    <div class="person">
      <p class="person__name">Colm Brestwick</p>
      <p class="person__title">Chief Executive Officer</p>
      <p class="person__line">cbrestwick@velkin-hartwell.example</p>
      <p class="person__line">Company No.: 7KQT58</p>
    </div>

    <div class="divider"></div>

    <div class="company">
      <p>Velkin Hartwell Ltd.</p>
      <p>27 Brenlow Court, Tullagesh,</p>
      <p>Kildare, Ireland, R9QT604.</p>
      <p class="company__row">
        <svg width="12" height="12" viewBox="0 0 24 24" aria-hidden="true"><path fill="#ffffff" d="M6.6 10.8a15.1 15.1 0 0 0 6.6 6.6l2.2-2.2a1 1 0 0 1 1-.25 11.4 11.4 0 0 0 3.6.57 1 1 0 0 1 1 1V20a1 1 0 0 1-1 1A17 17 0 0 1 3 4a1 1 0 0 1 1-1h3.5a1 1 0 0 1 1 1c0 1.250.2 2.450.57 3.57a1 1 0 0 1-.25 1z"/></svg>
        <span>00353-87-6207394</span>
      </p>
      <p class="company__row">
        <svg width="12" height="12" viewBox="0 0 24 24" aria-hidden="true"><circle cx="12" cy="12" r="10" fill="none" stroke="#ffffff" stroke-width="2.4"/><path d="M2 12h20M12 2c3 3 3 17 0 20M12 2c-3 3-3 17 0 20" fill="none" stroke="#ffffff" stroke-width="2"/></svg>
        <span>www.velkin-hartwell.example</span>
      </p>
    </div>
  </section>

  <section class="card card--back">
    <div class="wordmark"><span>Velkin Hartwell</span><span class="wordmark__dot"></span></div>
    <p class="site">www.velkin-hartwell.example</p>
  </section>
</main>
</body>
</html>
```